New Business Cards for NYC Salon

We are updating all of our cards. 7142-2869-4057 is my account number. We put names of our stylists on their cards. The back should include appointment space. Were looking for something more sleek and modern. Black/White Silver... or even touches of the orange color on our website which has been our thing for years. The design should communicate professional upscale boutique salon for men and women. Should be able to incorporate design into thank you cards, referral cards, brochure and postcards. The file is a zip file...we like the stacked ones black or white or the side versions.

Industry/Entity Type

Beauty Salon

Contact Information for Business Card

Marcus Dell's Salon313 W. 53rd Street, New York NY 10019 212-386-7714 info@marcusdellsalon.example www.marcusdellsalon.example

Font styles to use
Other font styles liked:
• trajan

Requirements
Must have
• we print a different card for every person in the salon. Begin by designing with the name Marcus. We will change it with every employee when printing. Must have a space for appointment date and time.
Nice to have
• Were looking to move towards the stacked or side placed logo but not opposed to utilizing the circular.
Should not have
• Photos

```html
<!DOCTYPE html>
<html lang="en">
<head>
<meta charset="utf-8">
<title>Marcus Dell's Salon — Business Cards</title>
<link rel="stylesheet" href="https://fonts.googleapis.com/css2?family=Questrial&display=swap">
<style>
  :root {
    --teal: #2bb9b1;
    --teal-deep: #22a39c;
    --charcoal: #3b3a3f;
    --ink: #4a4a4e;
    --rule: #b9b9bd;
    --paper: #ffffff;
    --backdrop: #ececea;
    --card-w: 520px;
    --card-h: 297px;
  }
  * { box-sizing: border-box; margin: 0; padding: 0; }
  html, body {
    width: 1200px;
    height: 892px;
    overflow: hidden;
    background: var(--backdrop);
    font-family: "Questrial", "Century Gothic", sans-serif;
    color: var(--ink);
  }
  .sheet { position: relative; width: 1200px; height: 892px; }

  .card {
    position: absolute;
    width: var(--card-w);
    height: var(--card-h);
    background: var(--paper);
    overflow: hidden;
    box-shadow: 0 6px 18px rgba(0,0,0,0.12);
  }
  .card-contact { left: 50px;  top: 298px; }
  .card-logo    { left: 630px; top: 298px; }
  .card svg.bands { position: absolute; inset: 0; width: 100%; height: 100%; }

  /* Wordmark */
  .wordmark {
    position: absolute;
    text-transform: uppercase;
    white-space: nowrap;
    display: flex;
    align-items: center;
    gap: 10px;
  }
  .wordmark .dot { display: inline-block; border-radius: 50%; background: var(--teal); flex: none; }
  .wordmark .name-stack { display: flex; flex-direction: column; align-items: center; }
  .wordmark .name-line { letter-spacing: 0.28em; }
  .wordmark .sub-line { letter-spacing: 0.3em; }

  .card-logo .wordmark {
    left: 0; right: 0; top: 58px;
    justify-content: center;
    color: var(--charcoal);
  }
  .card-logo .wordmark .dot { width: 12px; height: 12px; }
  .card-logo .wordmark .name-line { font-size: 22px; }
  .card-logo .wordmark .sub-line { font-size: 11px; margin-top: 4px; }

  .card-contact .wordmark { left: 34px; top: 62px; color: var(--teal); }
  .card-contact .wordmark .dot { width: 8px; height: 8px; }
  .card-contact .wordmark .name-line { font-size: 12px; letter-spacing: 0.24em; }
  .card-contact .wordmark .sub-line { font-size: 7px; margin-top: 3px; }

  /* Appointment space */
  .appointment {
    position: absolute;
    left: 60px; right: 60px; top: 136px;
    display: flex;
    gap: 28px;
    font-size: 9px;
    letter-spacing: 0.16em;
    text-transform: uppercase;
    color: var(--ink);
  }
  .appointment .field { flex: 1; display: flex; flex-direction: column; gap: 22px; }
  .appointment .field.wide { flex: 1.6; }
  .appointment .line { border-bottom: 1px solid var(--rule); height: 0; }

  /* Contact side */
  .stylist-name {
    position: absolute;
    right: 22px; top: 56px;
    font-size: 14px;
    color: var(--paper);
    letter-spacing: 0.03em;
  }
  .salon-block { position: absolute; left: 268px; top: 110px; }
  .salon-name {
    font-size: 17px;
    text-transform: uppercase;
    color: var(--teal);
    letter-spacing: 0.02em;
  }
  .salon-address { margin-top: 4px; font-size: 9.5px; color: var(--ink); }
  .contact-list {
    position: absolute;
    left: 150px; top: 188px;
    list-style: none;
    font-size: 9px;
    line-height: 1.55;
    color: var(--ink);
  }
</style>
</head>
<body>
<main class="sheet">

  <section class="card card-contact" aria-label="Business card, contact side">
    <svg class="bands" viewBox="0 0 520 297" aria-hidden="true">
      <rect x="0" y="0" width="520" height="16" fill="var(--teal)"/>
      <path d="M250 16 C 262 16, 262 48, 280 48 L 520 48 L 520 16 Z" fill="var(--teal)"/>
      <path d="M272 48 C 280 48, 282 82, 296 82 L 520 82 L 520 48 Z" fill="var(--charcoal)"/>
      <rect x="0" y="272" width="520" height="9" fill="var(--teal)"/>
      <rect x="0" y="281" width="520" height="16" fill="var(--charcoal)"/>
    </svg>
    <div class="wordmark">
      <span class="dot"></span>
      <span class="name-stack"><span class="name-line">Marcus Dell's</span><span class="sub-line">Salon</span></span>
    </div>
    <div class="stylist-name">Marcus Dell</div>
    <div class="salon-block">
      <div class="salon-name">Marcus Dell's Salon</div>
      <div class="salon-address">313 W. 53rd Street, New York NY 10019</div>
    </div>
    <ul class="contact-list">
      <li>212-386-7714</li>
      <li>info@marcusdellsalon.example</li>
      <li>www.marcusdellsalon.example</li>
    </ul>
  </section>

  <section class="card card-logo" aria-label="Business card, logo side with appointment space">
    <svg class="bands" viewBox="0 0 520 297" aria-hidden="true">
      <rect x="0" y="258" width="520" height="39" fill="var(--charcoal)"/>
      <path d="M0 206 L 396 206 C 418 206, 418 236, 440 236 L 520 236 L 520 262 L 0 262 Z" fill="var(--teal)"/>
      <path d="M0 222 L 0 206 L 6 206 Z" fill="var(--teal-deep)"/>
    </svg>
    <div class="wordmark">
      <span class="dot"></span>
      <span class="name-stack"><span class="name-line">Marcus Dell's</span><span class="sub-line">Salon</span></span>
    </div>
    <div class="appointment">
      <div class="field wide"><span>Appointment Date</span><span class="line"></span></div>
      <div class="field"><span>Time</span><span class="line"></span></div>
    </div>
  </section>

</main>
</body>
</html>
```